1 Home page redesign for existing repair service site.

We need a refresh of our existing website that looks more 2017. We have made a mockup of the content that we want and a sample of where we want it. Nothing is set in stone, if you have better ideas of where things should go, feel free.

You can see our current site at http://www.tokelmo.gr

The colors should stay orange/black/grey.

In many of the "boxes/banners" we will need images. Feel free to find in glade barn as we have an account.

We have made notes throughout the wireframe that we have attached on what we are looking for. Let us know if you have any questions. Thanks.

Target Market(s)

People using technology and breaking it

Industry/Entity Type

It Service

Number of Pages Required

1 page

Font styles to use
Sans Serif

Requirements
Must have
• Must have a modern, professional look and feel. Need custom graphics and icons.

```html
<!DOCTYPE html>
<html lang="en">
<head>
<meta charset="utf-8">
<title>Tokelmo – Device Repair</title>
<link href="https://fonts.googleapis.com/css2?family=Exo+2:wght@400;600;700;800&family=Roboto:wght@400;500;700&display=swap" rel="stylesheet">
<style>
:root{
  --orange:#f7931e;
  --orange-dark:#e07b0c;
  --black:#1c1c1c;
  --dark:#2b2b2b;
  --mid:#3a3a3a;
  --grey:#8a8a8a;
  --light:#ececec;
  --panel:#f4f4f4;
  --white:#ffffff;
  --text:#333333;
}
*{box-sizing:border-box;margin:0;padding:0}
html,body{width:1200px;height:3789px;overflow:hidden}
body{position:relative;background:var(--white);font-family:"Roboto",Arial,sans-serif;color:var(--text)}
.abs{position:absolute}
.display{font-family:"Exo 2","Roboto",sans-serif;text-transform:uppercase;letter-spacing:.5px}
.accent{color:var(--orange)}

/* top bar */
.topbar{left:0;top:0;width:1200px;height:33px;background:var(--black);color:#ccc;font-size:13px}
.topbar .quick{left:81px;top:0;height:33px;padding:0 18px;background:#333;line-height:33px;font-weight:500;color:#ddd}
.topbar .langs{left:770px;top:0;line-height:33px;font-size:12px;display:flex;gap:12px}
.topbar .social{left:860px;top:8px;display:flex;gap:15px}
.topbar .social span{width:17px;height:17px;border-radius:3px;background:#555;display:block}

/* header */
.header{left:0;top:33px;width:1200px;height:119px;background:var(--white)}
.brand{left:81px;top:30px;display:flex;align-items:center;gap:14px}
.brand-mark{width:46px;height:46px;background:var(--orange);border-radius:6px}
.brand-name{font-family:"Exo 2",sans-serif;font-weight:700;font-size:44px;color:var(--black)}
.nav{left:440px;top:44px;display:flex;gap:46px}
.nav a{font-family:"Exo 2",sans-serif;font-size:15px;font-weight:600;color:var(--black);text-decoration:none;text-transform:uppercase;text-align:center;border-bottom:2px solid var(--orange);padding-bottom:3px}
.phone{left:780px;top:46px;display:flex;align-items:center;gap:10px;font-size:21px;font-weight:700;color:var(--black);white-space:nowrap}
.live-chat{left:1005px;top:38px;width:115px;height:44px;border:2px solid var(--orange);border-radius:4px;font-family:"Exo 2",sans-serif;font-weight:700;color:var(--orange);font-size:15px;display:flex;align-items:center;justify-content:center;gap:8px;white-space:nowrap}

/* hero */
.hero{left:0;top:152px;width:1200px;height:366px;background:linear-gradient(100deg,#3b2a20 0%,#1e1a18 45%,#2a2624 70%,#141414 100%)}
.hero-title{right:80px;top:208px;text-align:right;color:var(--white)}
.hero-title h1{font-family:"Exo 2",sans-serif;font-weight:800;font-size:38px;text-transform:uppercase;line-height:1.1}
.hero-title p{font-family:"Exo 2",sans-serif;font-weight:700;font-size:27px}

/* counter band */
.counter{left:0;top:525px;width:1200px;height:81px;background:var(--black);border-top:3px solid #444}
.digits{left:81px;top:22px;display:flex;gap:6px}
.digits span{width:34px;height:36px;background:#fafafa;color:var(--black);font-family:"Exo 2",sans-serif;font-weight:700;font-size:24px;display:flex;align-items:center;justify-content:center;border-radius:3px}
.counter p{left:280px;top:26px;color:var(--white);font-size:20px;font-weight:600;white-space:nowrap;letter-spacing:.3px}

/* promo */
.promo{top:637px;width:508px;height:278px;background:var(--mid);display:flex}
.promo .media{width:250px;height:278px}
.promo .copy{flex:1;padding:26px 20px;text-align:center;color:var(--white)}
.promo h2{font-size:28px;font-weight:700;color:var(--orange);line-height:1.1}
.promo .sub{font-size:16px;margin-top:20px;line-height:1.4}
.btn{display:inline-block;background:var(--orange);color:var(--white);font-weight:700;font-size:15px;padding:11px 26px;text-transform:uppercase}
.promo .small{font-size:12px;color:#ccc;margin-top:24px;line-height:1.4}
.promo.right .copy{text-align:right}
.promo.right h2{text-align:right}

/* feature cards */
.feature{top:947px;width:243px;height:291px;background:linear-gradient(160deg,#3a3a3a,#161616);border:6px solid #1a1a1a}
.feature .frame{position:absolute;inset:6px;border:2px solid #777}
.feature .icon{position:absolute;left:0;right:0;top:30px;display:flex;justify-content:center}
.feature h3{position:absolute;left:10px;right:10px;top:112px;text-align:center;font-size:17px;font-weight:700;color:var(--orange);line-height:1.15}
.feature p{position:absolute;left:18px;right:18px;top:170px;text-align:center;font-size:13px;color:#ccc;line-height:1.4}
.plus{position:absolute;left:50%;bottom:-20px;transform:translateX(-50%);width:36px;height:36px;border-radius:50%;background:var(--orange);color:var(--white);font-size:24px;font-weight:700;display:flex;align-items:center;justify-content:center}

/* what we repair */
.repair-panel{left:81px;top:1308px;width:1038px;height:592px;background:var(--panel);border:3px solid #e2e2e2}
.section-title{left:0;width:1200px;text-align:center;font-size:30px;font-weight:700;color:var(--black)}
.tile{width:101px;height:101px;background:var(--dark);border:3px solid #111;display:flex;align-items:center;justify-content:center}
.tile.active{background:var(--orange);border-color:var(--orange-dark)}
.tile-label{width:200px;text-align:center;font-size:18px;color:var(--black)}
.tile-label.active{color:var(--orange)}

/* repair options */
.option{top:2014px;display:flex;align-items:center;gap:20px;font-size:20px;font-weight:600;color:var(--black);white-space:nowrap}
.option .sq{width:66px;height:66px;background:var(--orange);display:flex;align-items:center;justify-content:center}

/* why choose */
.why{top:2207px;width:242px;height:303px;background:linear-gradient(160deg,#3d3d3d,#121212);border:6px solid #1a1a1a;display:flex;align-items:center;justify-content:center;text-align:center;color:var(--orange);font-size:18px;font-weight:700;padding:0 18px;line-height:1.2}
.why.orange{background:var(--orange);border-color:#c76a0a;color:var(--white)}
.why .frame{position:absolute;inset:6px;border:2px solid rgba(255,255,255,.45)}
.arrow{top:2340px;font-size:40px;color:var(--grey);font-family:"Roboto",sans-serif}

/* testimonials */
.review{top:2640px;width:330px}
.review h4{font-size:15px;font-weight:700;color:var(--orange)}
.review ul{list-style:none;margin-top:10px;font-size:13px;color:#444}
.review li{display:flex;align-items:center;gap:8px;margin-bottom:6px;padding-left:14px}
.quote-box{position:absolute;top:63px;left:0;width:330px;height:278px;background:var(--light)}
.quote-box::after{content:"";position:absolute;left:40px;bottom:-20px;border-left:20px solid transparent;border-right:20px solid transparent;border-top:20px solid var(--light)}
.quote-badge{position:absolute;left:24px;top:30px;width:56px;height:56px;border-radius:50%;background:var(--orange);color:var(--white);font-family:Georgia,serif;font-size:44px;font-weight:700;display:flex;align-items:center;justify-content:center;padding-top:14px}
.quote-box p{position:absolute;left:70px;right:24px;top:98px;font-size:12px;line-height:1.45;color:#444}
.reviewer{position:absolute;top:380px;left:20px;font-size:16px;font-weight:700;color:var(--orange)}
.stars{position:absolute;top:406px;left:20px;color:var(--orange);font-size:14px;letter-spacing:2px}
.stars i{color:#888;font-style:normal}
.cta{left:447px;top:3170px;width:306px;height:48px;background:var(--orange);color:var(--white);font-size:16px;font-weight:700;display:flex;align-items:center;justify-content:center}

/* footer */
.footer{left:0;top:3284px;width:1200px;height:454px;background:#222}
.f-col{top:40px;color:#ddd}
.f-col h5{font-family:"Exo 2",sans-serif;font-size:16px;font-weight:700;color:var(--white);text-transform:uppercase;padding-bottom:12px;border-bottom:1px solid #444;margin-bottom:18px}
.f-col ul{list-style:none;font-size:13px;line-height:2.2}
.f-col li::before{content:"•";color:var(--orange);margin-right:8px}
.post{display:flex;gap:14px;margin-bottom:14px;align-items:flex-start}
.date{width:50px;height:50px;background:var(--orange);color:var(--white);text-align:center;font-weight:700;font-size:18px;line-height:1.1;padding-top:6px;flex-shrink:0}
.date small{display:block;font-size:11px}
.post p{font-size:13px;line-height:1.5;color:#ddd}
.news p{font-size:13px;line-height:1.5}
.email{margin-top:30px;width:225px;height:28px;background:var(--white);color:#777;font-size:12px;padding:6px 10px}
.subscribe{margin-top:16px;width:130px;height:40px;background:var(--orange);color:var(--white);font-weight:700;display:flex;align-items:center;justify-content:center;font-size:15px}
.follow li{list-style:none;display:flex;align-items:center;gap:10px;font-size:12px;line-height:1;margin-bottom:12px}
.follow li::before{content:none}
.follow .dot{width:20px;height:20px;border-radius:50%;border:1px solid #888;display:block}
.contact{top:3636px;display:flex;gap:14px;color:#ddd;font-size:13px;line-height:1.4}
.contact strong{display:block;font-size:16px;font-weight:500;color:var(--white)}
.contact em{font-style:normal;color:var(--orange)}
.contact .ring{width:34px;height:34px;border-radius:50%;border:2px solid var(--orange);display:flex;align-items:center;justify-content:center;flex-shrink:0}
.bottom{left:0;top:3738px;width:1200px;height:51px;background:var(--orange);color:var(--white);font-size:13px}
.bottom .copy{left:81px;top:17px}
.cards{right:81px;top:10px;display:flex;gap:8px;align-items:center}
.cards span.label{margin-right:8px;font-size:15px}
.card{width:58px;height:30px;background:var(--white);color:var(--black);font-size:11px;font-weight:700;display:flex;align-items:center;justify-content:center}
</style>
</head>
<body>

<!-- top bar -->
<div class="abs topbar">
  <div class="abs quick">QUICK LINKS &#8964;</div>
  <div class="abs langs"><span>GRE</span><span>ENG</span></div>
  <div class="abs social"><span></span><span></span><span></span><span></span><span></span><span></span><span></span><span></span></div>
</div>

<!-- header -->
<header class="abs header">
  <div class="abs brand"><span class="brand-mark"></span><span class="brand-name">Tokelmo</span></div>
  <nav class="abs nav"><a>Repairs</a><a>20 Stores</a><a>Blog</a></nav>
  <div class="abs phone">
    <svg width="30" height="27" viewBox="0 0 34 30"><path d="M4 10c0-5 26-5 26 0v4h-7v-3H11v3H4z" fill="#f7931e"/><rect x="7" y="15" width="20" height="13" rx="2" fill="#f7931e"/><circle cx="17" cy="21" r="3" fill="#fff"/></svg>
    210.555.0142
  </div>
  <div class="abs live-chat">
    <svg width="20" height="20" viewBox="0 0 22 20"><circle cx="11" cy="10" r="9" fill="#f7931e"/></svg>LIVE CHAT
  </div>
</header>

<!-- hero -->
<section class="abs hero" role="img" aria-label="Photo of a Tokelmo storefront sign at night"></section>
<div class="abs hero-title"><h1>20 Nationwide Locations</h1><p>there is a Tokelmo near you</p></div>

<!-- counter -->
<section class="abs counter">
  <div class="abs digits"><span>0</span><span>1</span><span>2</span><span>3</span><span>4</span></div>
  <p class="abs display">Repairs completed with happy customers. Yep, we fix a lot of devices!</p>
</section>

<!-- promos -->
<section class="abs promo" style="left:81px">
  <div class="media" role="img" aria-label="Hand holding a smartphone showing a store map" style="background:linear-gradient(135deg,#c9cfc8,#8d948c)"></div>
  <div class="copy">
    <h2 class="display">20 Locations</h2>
    <p class="sub display" style="margin-top:20px;font-size:17px">Find a store near you</p>
    <div style="margin-top:70px"><span class="btn display">View Map &raquo;</span></div>
  </div>
</section>
<section class="abs promo right" style="left:606px">
  <div class="media" role="img" aria-label="Gold best price guarantee seal over a workshop photo" style="background:linear-gradient(135deg,#9a8f83,#5d554d)"></div>
  <div class="copy">
    <h2 class="display">Low Price<br>Guarantee</h2>
    <p class="sub">Find a lower price for your Fonix or Tabix repair? We will match it!</p>
    <p class="small">* Terms and conditions apply,<br>click to read more</p>
  </div>
</section>

<!-- feature cards -->
<div class="abs feature" style="left:81px"><div class="frame"></div>
  <div class="icon"><svg width="54" height="60" viewBox="0 0 54 60" fill="none" stroke="#fff" stroke-width="4"><rect x="6" y="4" width="28" height="52" rx="4"/><path d="M40 8l10 10M46 4v20"/></svg></div>
  <h3 class="display">Open Service Area</h3>
  <p>Repairs right in front of you, no closed doors, no back rooms</p>
  <div class="plus">+</div></div>
<div class="abs feature" style="left:346px"><div class="frame"></div>
  <div class="icon"><svg width="60" height="60" viewBox="0 0 60 60"><circle cx="30" cy="30" r="26" fill="none" stroke="#fff" stroke-width="3"/><text x="30" y="35" text-anchor="middle" fill="#fff" font-size="14" font-family="Roboto">50-75%</text></svg></div>
  <h3 class="display">Save 50-75%<br>on multiple repairs</h3>
  <p>If your device needs more than 1 part replaced, save up to 75% on addition parts.</p>
  <div class="plus">+</div></div>
<div class="abs feature" style="left:610px"><div class="frame"></div>
  <div class="icon"><svg width="60" height="60" viewBox="0 0 60 60" fill="none" stroke="#fff" stroke-width="4"><rect x="20" y="4" width="22" height="40" rx="3"/><path d="M8 30v24M52 30v24M8 54h44"/></svg></div>
  <h3 class="display">Accessories</h3>
  <p>Lorem ipsum dolor sit amet, consectetuer adipiscing.</p>
  <div class="plus">+</div></div>
<div class="abs feature" style="left:876px"><div class="frame"></div>
  <div class="icon"><svg width="60" height="60" viewBox="0 0 60 60" fill="none" stroke="#fff" stroke-width="4"><circle cx="30" cy="32" r="24"/><path d="M30 18v14h10M24 4h12"/></svg></div>
  <h3 class="display">20 Minute Repairs</h3>
  <p>Lorem ipsum dolor sit amet, consectetuer adipiscing.</p>
  <div class="plus">+</div></div>

<!-- what we repair -->
<section class="abs repair-panel"></section>
<h2 class="abs section-title display" style="top:1355px"><span class="accent">What</span> we repair</h2>

<div class="abs tile active" style="left:124px;top:1435px"><svg width="34" height="60" viewBox="0 0 34 60" fill="none" stroke="#fff" stroke-width="3"><rect x="2" y="2" width="30" height="56" rx="5"/><path d="M2 10h30M2 48h30"/></svg></div>
<div class="abs tile" style="left:328px;top:1435px"><svg width="50" height="62" viewBox="0 0 50 62" fill="none" stroke="#fff" stroke-width="3"><rect x="2" y="2" width="46" height="58" rx="5"/><rect x="8" y="8" width="34" height="44"/></svg></div>
<div class="abs tile" style="left:533px;top:1435px"><svg width="40" height="62" viewBox="0 0 40 62"><rect x="1" y="1" width="38" height="60" rx="5" fill="#fff"/><rect x="6" y="6" width="28" height="20" fill="#2b2b2b"/><circle cx="20" cy="43" r="11" fill="#2b2b2b"/><circle cx="20" cy="43" r="4" fill="#fff"/></svg></div>
<div class="abs tile" style="left:738px;top:1435px"><svg width="36" height="62" viewBox="0 0 36 62" fill="none" stroke="#fff" stroke-width="3"><rect x="2" y="2" width="32" height="58" rx="5"/><path d="M2 10h32M2 50h32"/></svg></div>
<div class="abs tile" style="left:942px;top:1435px"><svg width="42" height="64" viewBox="0 0 42 64"><rect x="1" y="1" width="40" height="62" rx="8" fill="#fff"/><rect x="6" y="7" width="30" height="20" fill="#2b2b2b"/><g fill="#2b2b2b"><rect x="7" y="34" width="6" height="4"/><rect x="18" y="34" width="6" height="4"/><rect x="29" y="34" width="6" height="4"/><rect x="7" y="43" width="6" height="4"/><rect x="18" y="43" width="6" height="4"/><rect x="29" y="43" width="6" height="4"/><rect x="7" y="52" width="6" height="4"/><rect x="18" y="52" width="6" height="4"/><rect x="29" y="52" width="6" height="4"/></g></svg></div>

<div class="abs tile-label active" style="left:75px;top:1590px">Fonix Repair</div>
<div class="abs tile-label" style="left:279px;top:1590px">Tabix Repair</div>
<div class="abs tile-label" style="left:484px;top:1590px">Podix Touch Repair</div>
<div class="abs tile-label" style="left:689px;top:1590px">Samtrel Repair</div>
<div class="abs tile-label" style="left:893px;top:1590px">Berrytel Repair</div>

<div class="abs tile" style="left:124px;top:1672px"><svg width="64" height="56" viewBox="0 0 64 56" fill="none" stroke="#fff" stroke-width="3"><rect x="2" y="2" width="60" height="40" rx="3"/><path d="M26 42l-4 12h20l-4-12"/></svg></div>
<div class="abs tile" style="left:328px;top:1672px"><svg width="70" height="46" viewBox="0 0 70 46" fill="none" stroke="#fff" stroke-width="3"><rect x="10" y="2" width="50" height="34" rx="2"/><path d="M2 40h66"/></svg></div>
<div class="abs tile" style="left:533px;top:1672px"><svg width="70" height="56" viewBox="0 0 70 56" fill="none" stroke="#fff" stroke-width="3"><rect x="2" y="2" width="46" height="34" rx="2"/><path d="M18 46h14M25 36v10"/><rect x="54" y="4" width="14" height="46"/></svg></div>
<div class="abs tile" style="left:738px;top:1672px"><svg width="70" height="48" viewBox="0 0 70 48" fill="none" stroke="#fff" stroke-width="3"><rect x="10" y="2" width="50" height="34" rx="2"/><path d="M2 42h66"/></svg></div>
<div class="abs tile" style="left:942px;top:1672px"><svg width="60" height="62" viewBox="0 0 60 62"><rect x="2" y="4" width="20" height="14" rx="3" fill="#fff"/><circle cx="30" cy="22" r="10" fill="#fff"/><path d="M10 62c0-18 10-26 20-26s20 8 20 26z" fill="#fff"/><path d="M30 38l-3 6 3 14 3-14z" fill="#2b2b2b"/></svg></div>

<div class="abs tile-label" style="left:75px;top:1830px">Deskix Repairs</div>
<div class="abs tile-label" style="left:279px;top:1830px">Bookix Repair</div>
<div class="abs tile-label" style="left:484px;top:1830px">Computer Repair</div>
<div class="abs tile-label" style="left:689px;top:1830px">Laptop Repair</div>
<div class="abs tile-label" style="left:893px;top:1830px">Business Services</div>

<!-- repair options -->
<h2 class="abs section-title display" style="top:1945px"><span class="accent">Repair</span> options</h2>
<div class="abs option" style="left:81px"><span class="sq"><svg width="44" height="30" viewBox="0 0 44 30" fill="#fff"><rect x="0" y="4" width="26" height="18"/><path d="M28 10h9l6 7v5H28z"/><circle cx="8" cy="25" r="4"/><circle cx="35" cy="25" r="4"/></svg></span>FIND A STORE NEAR YOU?</div>
<div class="abs option" style="left:447px"><span class="sq"><svg width="34" height="38" viewBox="0 0 34 38" fill="#fff"><rect x="2" y="12" width="30" height="26"/><path d="M10 12V8a7 7 0 0 1 14 0v4" fill="none" stroke="#fff" stroke-width="3"/></svg></span>SEND US YOUR DEVICE?</div>
<div class="abs option" style="left:798px"><span class="sq"><svg width="40" height="40" viewBox="0 0 40 40"><circle cx="20" cy="20" r="17" fill="none" stroke="#fff" stroke-width="3"/><text x="20" y="28" text-anchor="middle" fill="#fff" font-size="22" font-weight="700" font-family="Roboto">$</text></svg></span>FREE PICKUP IN ATHENS</div>

<!-- why choose -->
<h2 class="abs section-title display" style="top:2140px"><span class="accent">Why</span> choose <span class="accent">Tokelmo</span></h2>
<div class="abs arrow" style="left:38px">&lsaquo;</div>
<div class="abs arrow" style="left:1146px">&rsaquo;</div>
<div class="abs why orange display" style="left:81px" role="img" aria-label="Technician working on a circuit board, orange tinted"><div class="frame"></div>Open Service Area</div>
<div class="abs why display" style="left:345px" role="img" aria-label="Repair bench photo, dark tinted"><div class="frame"></div>Save 50-75%<br>on multiple repairs</div>
<div class="abs why display" style="left:609px" role="img" aria-label="Accessories photo, dark tinted"><div class="frame"></div>Accessories</div>
<div class="abs why display" style="left:873px" role="img" aria-label="Urgent care repair sign photo, dark tinted"><div class="frame"></div>20 Minute Repairs</div>

<!-- testimonials -->
<h2 class="abs section-title display" style="top:2562px"><span class="accent">What our</span> customers say</h2>
<div class="abs arrow" style="left:38px;top:2860px">&lsaquo;</div>
<div class="abs arrow" style="left:1146px;top:2860px">&rsaquo;</div>

<article class="abs review" style="left:81px">
  <h4>Laptop Repair</h4>
  <ul><li><span class="accent">&#10003;</span>Overheating</li></ul>
  <div class="quote-box"><div class="quote-badge">&ldquo;</div>
    <p>or months my laptop was in meltdown mode. It was terribly slow and I was getting error messages and frequent shutdowns. Since my whole life is on it I was desperate for a better solution because I didn't want to say goodbye to my laptop or my files. Tokelmo saved all my precious files and now my computer is really fast! I recommend them without any hesitation. You guys are fantastic!</p></div>
  <div class="reviewer">Eleni M., Chalandri</div>
  <div class="stars">&#9733;&#9733;&#9733;&#9733;<i>&#9733;</i></div>
</article>
<article class="abs review" style="left:434px">
  <h4>Fonix 5 Repair</h4>
  <ul><li><span class="accent">&#10003;</span>Water Damage Repair</li><li><span class="accent">&#10003;</span>Dock Connector Replacement</li></ul>
  <div class="quote-box"><div class="quote-badge">&ldquo;</div>
    <p>My Fonix 5 took a dive in the deep end of the pool and it never crossed my mind that it could be saved! Congratulations, you fixed it!</p></div>
  <div class="reviewer">Nikos P., Thessaloniki</div>
  <div class="stars">&#9733;&#9733;&#9733;&#9733;<i>&#9733;</i></div>
</article>
<article class="abs review" style="left:789px">
  <h4>Fonix 6 Repair</h4>
  <ul><li><span class="accent">&#10003;</span>Screen Replacement</li></ul>
  <div class="quote-box"><div class="quote-badge">&ldquo;</div>
    <p>I just can't part with my Fonix ... I can't do anything without it! When my screen broke I went to Tokelmo feeling helpless. They replaced the screen incredibly fast in only 15 minutes!!! I was relieved, excited and grateful! Thank you is not enough!</p></div>
  <div class="reviewer">Sofia K., Peristeri</div>
  <div class="stars">&#9733;&#9733;&#9733;&#9733;<i>&#9733;</i></div>
</article>
<div class="abs cta">Tell us about your Tokelmo experience</div>

<!-- footer -->
<footer class="abs footer">
  <div class="abs f-col" style="left:81px;width:240px">
    <h5>Quick Links</h5>
    <ul><li>About Tokelmo</li><li>Business Services</li><li>Schedule a Pickup</li><li>Job openings</li><li>Shipping Instructions</li><li>Privacy policy</li><li>Send your device with PointCourier</li></ul>
  </div>
  <div class="abs f-col" style="left:366px;width:300px">
    <h5>Tokelmo Blog Posts</h5>
    <div class="post"><div class="date">12<small>MAR</small></div><p>Lorem ipsum dolor sit amet lotre is consectetuer adipiscing elit .</p></div>
    <div class="post"><div class="date">12<small>MAR</small></div><p>Lorem ipsum dolor sit amet lotre is consectetuer adipiscing elit .</p></div>
    <div class="post"><div class="date">12<small>MAR</small></div><p>Lorem ipsum dolor sit amet lotre is consectetuer adipiscing elit .</p></div>
  </div>
  <div class="abs f-col news" style="left:730px;width:240px">
    <h5>News Letter</h5>
    <p><strong>Subscribe to the Tokelmo newsletter</strong></p>
    <p>Lorem ipsum dolor sit amet lotre is consectetuer adipiscing elit .</p>
    <div class="email">Email Address</div>
    <div class="subscribe">SUBSCRIBE &raquo;</div>
  </div>
  <div class="abs f-col follow" style="left:1017px;width:110px">
    <h5>Follow Us</h5>
    <ul>
      <li><span class="dot"></span>Facenet</li><li><span class="dot"></span>Chirper</li><li><span class="dot"></span>Linkpro</li><li><span class="dot"></span>Vidstream</li><li><span class="dot"></span>Snapgram</li><li><span class="dot"></span>Pinboard</li><li><span class="dot"></span>Circleplus</li>
    </ul>
  </div>
</footer>

<div class="abs contact" style="left:81px"><span class="ring"><svg width="16" height="12" viewBox="0 0 16 12" fill="none" stroke="#f7931e" stroke-width="2"><rect x="1" y="1" width="14" height="10"/><path d="M1 1l7 6 7-6"/></svg></span><div><strong>Email Support</strong>We usually respond within 24 hours<br><em>Click to send email</em></div></div>
<div class="abs contact" style="left:447px"><span class="ring"><svg width="16" height="16" viewBox="0 0 16 16" fill="#f7931e"><path d="M3 1l3 3-2 2c1 2 3 4 5 5l2-2 3 3-2 3C6 14 2 10 1 3z"/></svg></span><div><strong>Contact our call center</strong>Call to speak to a customer service rep.<br><em>210.555.0142</em></div></div>
<div class="abs contact" style="left:860px"><span class="ring"><svg width="16" height="14" viewBox="0 0 16 14" fill="#f7931e"><path d="M1 1h14v9H6l-4 3v-3H1z"/></svg></span><div><strong>LIVE CHAT</strong>Chat with a Tokelmo technician now.<br><em>Click to chat</em></div></div>

<div class="abs bottom">
  <div class="abs copy">Copyright &copy; 2017 Tokelmo. All Rights Reserved.</div>
  <div class="abs cards"><span class="label">We Accept:</span><span class="card">VEXA</span><span class="card">CARDMAX</span><span class="card">PAYMO</span></div>
</div>

</body>
</html>
```